Bright Path Run rare disease fundraising campaign

We need an original banner for a social media fundraising campaign for a the rare disease Neurofibromatosis Type 2. There is new therapy we are going to raise money to support research for and the concept is bacteria being genetically modified to kill the tumors caused by NF2. We had a previous fundraiser that including axe throwing and we call it bright path run. We want to build on this to create a fundraising banner with a tumor and little bacteria holding axes and starting to destroy the tumor. I have included the axe logo we used to the axes and fonts can be made to look similar.

Target Market(s)

donors who support research for children with rare diseases

Industry/Entity Type

Medical And Science

Font styles to use
Sans Serif

Colors
33a6d7

Requirements
Must have
• The blue bacteria cartoon is an example of that the bacteria should look like but they should be holding axes to chop up the tumor. It should be one tumor and 3-4 bacteria trying to destroy it with axes.

bacteria killing tumors with axes. Im not sure how best to portray a tumor but maybe something that looks like a troll or monster and label it "NF2 tumor"

Text should read "give today to help us bright path run"
Nice to have
• a David and Goliath type theme, there little guys (bacteria) taking down a big bad tumor.
Should not have
• The logo I attached is just to show what the axes in our campaign look like but should not be used as the image for the banner, that needs to be drawn.

```html
<!DOCTYPE html>
<html lang="en">
<head>
<meta charset="utf-8">
<title>Bright Path Run – Give Today Banners</title>
<link rel="stylesheet" href="https://fonts.googleapis.com/css2?family=Montserrat:wght@500;600;700&display=swap">
<style>
  :root {
    --stage: #5f5f5f;
    --sky: #4aa5d4;
    --navy: #21284a;
    --white: #ffffff;
    --pale: #d1e6f3;
    --mist: #c6c8d2;
    --germ-light: #2aa3ff;
    --germ-deep: #0a3bd6;
  }
  html, body {
    margin: 0;
    padding: 0;
    width: 1200px;
    height: 723px;
    overflow: hidden;
    background: var(--stage);
  }
  .sheet {
    display: block;
    width: 1200px;
    height: 723px;
  }
  .fill-sky { fill: var(--sky); }
  .fill-navy { fill: var(--navy); }
  .fill-white { fill: var(--white); }
  .fill-pale { fill: var(--pale); }
  .fill-mist { fill: var(--mist); }
  .label {
    font-family: "Montserrat", sans-serif;
    fill: var(--white);
  }
  .label-please { font-weight: 500; }
  .label-headline { font-weight: 700; }
  .label-sub { font-weight: 600; }
  .wordmark {
    font-family: "Montserrat", sans-serif;
    font-weight: 700;
    fill: var(--white);
  }
</style>
</head>
<body>
<svg class="sheet" viewBox="0 0 2464 1484" xmlns="http://www.w3.org/2000/svg">
  <defs>
    <radialGradient id="germ-tone" cx="40%" cy="35%" r="70%">
      <stop offset="0" stop-color="var(--germ-light)"/>
      <stop offset="1" stop-color="var(--germ-deep)"/>
    </radialGradient>
  </defs>

  <rect class="stage" width="2464" height="1484" fill="var(--stage)"/>

  <!-- Wide banner -->
  <g class="banner-wide">
    <rect class="fill-white" x="116" y="76" width="2232" height="575"/>
    <polygon class="fill-sky" points="441,76 1450,76 1520,310 1340,651 218,651"/>
    <polygon class="fill-navy" points="116,483 252,553 218,651 116,651"/>
    <polygon class="fill-white" points="1520,310 1628,651 1340,651"/>
    <polygon class="fill-navy" points="1450,76 2245,76 2212,172 2348,245 2348,651 1628,651"/>
    <polygon class="fill-sky" points="2245,76 2348,76 2348,245 2212,172"/>

    <rect class="fill-navy headline-pill" x="204" y="297" width="1236" height="134" rx="67"/>
    <text class="label label-please" x="822" y="286" font-size="36" text-anchor="middle">PLEASE</text>
    <text class="label label-headline" x="822" y="418" font-size="150" text-anchor="middle" textLength="1115" lengthAdjust="spacingAndGlyphs">GIVE TODAY</text>
    <text class="label label-sub" x="822" y="466" font-size="36" text-anchor="middle">TO HELP US BRIGHT PATH RUN</text>

    <g role="img" aria-label="Cartoon of a blue bacterium wielding an axe against the tumour">
      <rect x="1640" y="150" width="660" height="320" rx="140" fill="url(#germ-tone)"/>
    </g>
    <text class="wordmark" x="1960" y="545" font-size="78" text-anchor="middle">Bright Path Run</text>
  </g>

  <!-- Square banner, small -->
  <g class="banner-square-small">
    <rect class="fill-sky" x="385" y="840" width="690" height="574"/>
    <polygon class="fill-pale" points="385,840 523,840 565,948 385,952"/>
    <polygon class="fill-mist" points="385,952 565,948 560,965 385,1070"/>
    <polygon class="fill-navy" points="385,1070 560,965 930,962 1075,843 1075,1185 905,1290 545,1290 385,1414"/>
    <polygon class="fill-mist" points="905,1290 1075,1185 1075,1303"/>
    <polygon class="fill-pale" points="905,1290 1075,1303 1075,1414 938,1414"/>

    <text class="label label-please" x="471" y="942" font-size="20">PLEASE</text>
    <text class="label label-headline" x="471" y="1017" font-size="74" textLength="530" lengthAdjust="spacingAndGlyphs">GIVE TODAY</text>
    <text class="label label-sub" x="737" y="1055" font-size="21" text-anchor="middle">TO HELP US BRIGHT PATH RUN</text>

    <g role="img" aria-label="Cartoon of a blue bacterium wielding an axe against the tumour">
      <rect x="480" y="1065" width="500" height="190" rx="90" fill="url(#germ-tone)"/>
    </g>
    <text class="wordmark" x="725" y="1318" font-size="60" text-anchor="middle">Bright Path Run</text>
  </g>

  <!-- Square banner, large -->
  <g class="banner-square-large">
    <rect class="fill-sky" x="1242" y="726" width="691" height="688"/>
    <polygon class="fill-pale" points="1242,726 1380,726 1428,857 1242,840"/>
    <polygon class="fill-mist" points="1242,840 1428,857 1242,958"/>
    <polygon class="fill-navy" points="1242,958 1428,857 1748,885 1933,726 1933,1180 1748,1290 1405,1290 1242,1414"/>
    <polygon class="fill-mist" points="1748,1290 1933,1180 1933,1302"/>
    <polygon class="fill-pale" points="1748,1290 1933,1302 1933,1414 1795,1414"/>

    <text class="label label-please" x="1290" y="861" font-size="22">PLEASE</text>
    <text class="label label-headline" x="1290" y="945" font-size="82" textLength="593" lengthAdjust="spacingAndGlyphs">GIVE TODAY</text>
    <text class="label label-sub" x="1588" y="989" font-size="23" text-anchor="middle">TO HELP US BRIGHT PATH RUN</text>

    <g role="img" aria-label="Cartoon of a blue bacterium wielding an axe against the tumour">
      <rect x="1290" y="1000" width="580" height="215" rx="100" fill="url(#germ-tone)"/>
    </g>
    <text class="wordmark" x="1575" y="1280" font-size="68" text-anchor="middle">Bright Path Run</text>
  </g>
</svg>
</body>
</html>
```